K&T Fixit and Rebuild general contracting business card design

I already have a logo that I want to use and I need a card that uses that logo and color scheme on the front with the address phone numbers and email and on the back a place for technicians to write in their name and phone number when they hand it out. It will need the License number of License #KTFXTRB318QN.
It should say General Contractor under the company name. The address is
4417 NE 3rd St, Ste D226
Vancouver, WA 98652
www.kandtfixitandrebuild.example
office@kandtfixitandrebuild.example
360-555-0142 is the telephone number
360-555-0187 is the fax number

Target Market(s)

Homeowners needing remodel work or repairs in their home.

Industry/Entity Type

Construction

Contact Information for Business Card

Business name, address, phone number, license number, fax number, email, and website on the front and a place to fill in technician's name and number

Font styles to use
Serif

Requirements
Must have
• Business name, address, phone number, license number, fax number, email, and website on the front and a place to fill in technician's name and number
Nice to have
• I uploaded an example of a front that is good.
Should not have
• Froo froo or extra embellishments.

```html
<!DOCTYPE html>
<html lang="en">
<head>
<meta charset="utf-8">
<title>K&amp;T Fixit and Rebuild – Business Card</title>
<link href="https://fonts.googleapis.com/css2?family=Montserrat:wght@400;500;600&display=swap" rel="stylesheet">
<style>
  :root {
    --copper: #b0643a;
    --copper-dark: #94502b;
    --wood-light: #c98a5e;
    --wood-dark: #8f5434;
    --ink: #2b2b2b;
    --rule: #d2a88c;
    --paper: #ffffff;
    --backdrop: #3a3a3a;
  }
  * { box-sizing: border-box; margin: 0; padding: 0; }
  html, body { width: 1200px; height: 900px; overflow: hidden; }
  body {
    background: var(--backdrop);
    font-family: "Montserrat", sans-serif;
    color: var(--ink);
    position: relative;
  }
  .card {
    position: absolute;
    top: 100px;
    width: 400px;
    height: 700px;
    background: var(--paper);
    border-radius: 30px;
    overflow: hidden;
    text-align: center;
  }
  .card--front { left: 160px; }
  .card--back { left: 640px; }

  /* Front */
  .brand-mark {
    margin-top: 110px;
    font-size: 34px;
    font-weight: 600;
    color: var(--copper);
    line-height: 1.15;
    display: flex;
    align-items: center;
    justify-content: center;
    gap: 12px;
  }
  .brand-mark__square {
    width: 22px; height: 22px;
    background: var(--copper);
    flex: none;
  }
  .company-name {
    margin-top: 70px;
    font-size: 22px;
    font-weight: 500;
    color: var(--copper);
    text-transform: uppercase;
    letter-spacing: 0.5px;
  }
  .company-role {
    font-size: 19px;
    margin-top: 2px;
  }
  .icon-row {
    display: flex;
    align-items: center;
    justify-content: center;
    gap: 6px;
    margin-top: 24px;
  }
  .icon-row__rule {
    flex: 1;
    height: 1px;
    background: var(--rule);
    margin: 0 8px;
  }
  .icon-row .rule-left { margin-left: 30px; }
  .icon-row .rule-right { margin-right: 30px; }
  .contact-icon {
    width: 30px; height: 30px;
    border: 2px solid var(--copper);
    border-radius: 6px;
    display: flex; align-items: center; justify-content: center;
  }
  .contact-list {
    list-style: none;
    margin-top: 16px;
    font-size: 16px;
    line-height: 1.55;
  }
  .contact-list .web-domain { color: var(--copper); }
  .short-rule {
    width: 140px; height: 1px;
    background: var(--rule);
    margin: 16px auto 18px;
  }
  .address { font-style: normal; font-size: 16px; line-height: 1.4; }
  .license-band {
    position: absolute;
    left: 0; right: 0; bottom: 0;
    height: 64px;
    background: var(--copper);
    color: #fff;
    font-size: 18px;
    display: flex; align-items: center; justify-content: center;
    letter-spacing: 0.4px;
  }

  /* Back */
  .hero {
    height: 330px;
    background: linear-gradient(135deg, var(--wood-dark), var(--wood-light) 55%, var(--wood-dark));
    display: flex; align-items: center; justify-content: center;
  }
  .hero__name {
    color: #fff;
    font-size: 32px;
    font-weight: 600;
    line-height: 1.15;
    padding: 0 40px;
  }
  .fill-field { margin: 0 40px; }
  .fill-field__label {
    display: block;
    font-size: 18px;
    padding-top: 26px;
    padding-bottom: 42px;
  }
  .fill-field__line { height: 1px; background: #8a8a8a; }
  .fill-field--last .fill-field__line { margin-top: 70px; }
</style>
</head>
<body>

<article class="card card--front">
  <div class="brand-mark"><span class="brand-mark__square"></span><span>K&amp;T Fixit<br>and Rebuild</span></div>

  <h1 class="company-name">K&amp;T Fixit and Rebuild</h1>
  <p class="company-role">General Contractor</p>

  <div class="icon-row">
    <span class="icon-row__rule rule-left"></span>
    <span class="contact-icon" title="Phone">
      <svg width="16" height="16" viewBox="0 0 16 16"><path d="M3 2h3l1 3-2 1a8 8 0 0 0 5 5l1-2 3 1v3a1 1 0 0 1-1 1A12 12 0 0 1 2 3a1 1 0 0 1 1-1z" fill="var(--copper)"/></svg>
    </span>
    <span class="contact-icon" title="Fax">
      <svg width="16" height="16" viewBox="0 0 16 16"><rect x="4" y="1" width="8" height="5" fill="none" stroke="var(--copper)" stroke-width="1.5"/><rect x="1" y="6" width="14" height="8" rx="1" fill="var(--copper)"/></svg>
    </span>
    <span class="contact-icon" title="Email">
      <svg width="16" height="16" viewBox="0 0 16 16"><rect x="1" y="3" width="14" height="10" rx="1" fill="var(--copper)"/><path d="M1 4l7 5 7-5" fill="none" stroke="#fff" stroke-width="1.3"/></svg>
    </span>
    <span class="contact-icon" title="Website">
      <svg width="16" height="16" viewBox="0 0 16 16"><circle cx="8" cy="8" r="6.5" fill="none" stroke="var(--copper)" stroke-width="1.5"/><ellipse cx="8" cy="8" rx="2.8" ry="6.5" fill="none" stroke="var(--copper)" stroke-width="1.2"/><path d="M1.5 8h13" stroke="var(--copper)" stroke-width="1.2"/></svg>
    </span>
    <span class="icon-row__rule rule-right"></span>
  </div>

  <ul class="contact-list">
    <li>360-555-0142</li>
    <li>360-555-0187</li>
    <li>office@kandtfixitandrebuild.example</li>
    <li>www.<span class="web-domain">kandtfixitandrebuild.example</span></li>
  </ul>

  <div class="short-rule"></div>

  <address class="address">4417 NE 3rd St, Ste D226<br>Vancouver, WA 98652</address>

  <div class="license-band">License Number #KTFXTRB318QN</div>
</article>

<article class="card card--back">
  <div class="hero" role="img" aria-label="Wooden workbench with hammer, wrench, drill bits, tape measure and nails">
    <span class="hero__name">K&amp;T Fixit<br>and Rebuild</span>
  </div>
  <div class="fill-field">
    <span class="fill-field__label">Name</span>
    <div class="fill-field__line"></div>
  </div>
  <div class="fill-field">
    <span class="fill-field__label">Time and Date</span>
    <div class="fill-field__line"></div>
  </div>
  <div class="fill-field fill-field--last">
    <div class="fill-field__line"></div>
  </div>
</article>

</body>
</html>
```